Automotive Brand Survey Online

Hi guys, we are looking for a freelancer who can design User Interface design (UI) for a survey-online website layout. <br/><br/>For the content, there are question, choices, back and next buttons - as if you are designing a survey website.<br/><br/>There are 5 main contents of the website consists of:<br/>1. Single-answer question<br/>2. Yes/No-answer question<br/>3. Net Promoter Score (NPS) or 1-5 scale question<br/>4. Open-end question<br/>5. Thank you page when finish survey<br/><br/>Here is the demo and more description<br/>https://demo.quorvel.link/survey/
Target Market(s)
Car Owner
Industry/Entity Type
Automotive
Number of Pages Required
1 page

```html
<!DOCTYPE html>
<html lang="en">
<head>
<meta charset="utf-8">
<title>Survey Webpage Mobile Layout</title>
<link href="https://fonts.googleapis.com/css2?family=Montserrat:wght@400;500;600;700&display=swap" rel="stylesheet">
<style>
:root{
  --canvas:#f7f7f7;
  --heading:#4e5b78;
  --navy:#1f3653;
  --ink:#111;
  --green:#2f5a45;
  --mint:#8fd0ae;
  --screen-grey:#eeeef1;
  --screen-warm:#f3efec;
  --white:#fff;
  --track:#f1f1f3;
  --back:#8e1b24;
  --legal:#4a1f4f;
  --line:#9aa8b8;
}
*{box-sizing:border-box;margin:0;padding:0}
html,body{width:1200px;height:1066px;overflow:hidden;background:var(--canvas);font-family:"Montserrat",sans-serif}
.canvas{position:relative;width:1200px;height:1066px}
.page-title{position:absolute;top:24px;left:0;right:0;text-align:center;font-size:33px;font-weight:500;color:var(--heading);letter-spacing:.5px}
.page-label{position:absolute;font-size:12px;color:var(--heading);font-weight:500}

.screen{position:absolute;width:180px;background:var(--white);overflow:hidden;box-shadow:0 1px 4px rgba(0,0,0,.12)}
.screen .backdrop{position:absolute;top:0;left:0;width:180px;height:180px}
.screen .backdrop path{fill:var(--screen-grey)}
.screen.warm .backdrop path{fill:var(--screen-warm)}
.screen.warm .legal{background:var(--screen-warm)}
.screen > *{position:absolute}

.brand{top:14px;left:0;right:0;display:flex;flex-direction:column;align-items:center;gap:3px}
.brand-dot{width:16px;height:16px;border-radius:50%;background:var(--line)}
.brand-name{font-size:7px;font-weight:600;letter-spacing:1.5px;color:var(--line)}
.close{top:9px;right:6px;width:8px;height:8px}

.survey-title{top:56px;left:0;right:0;text-align:center;font-size:12px;font-weight:700;color:var(--ink);letter-spacing:.2px}
.question{top:80px;left:0;right:0;text-align:center;font-size:11px;font-weight:600;color:var(--navy);line-height:12px}

.answer-box{left:20px;top:121px;width:139px;height:72px;border:1px solid var(--green);border-radius:3px;background:#f8f8f8;box-shadow:0 2px 4px rgba(0,0,0,.15)}

.option{left:52px;width:75px;height:16px;border:1px solid var(--line);border-radius:3px;background:var(--white);font-size:6px;color:var(--navy);display:flex;align-items:center;padding-left:6px;gap:4px;white-space:nowrap}
.radio{width:6px;height:6px;border-radius:50%;border:1px solid var(--navy);flex:none}
.option.wide{left:15px;width:151px;background:var(--green);color:var(--white);border-color:var(--green);box-shadow:0 2px 4px rgba(0,0,0,.2)}
.option.wide .radio{border:1.5px solid var(--white)}

.choice{left:45px;width:90px;height:21px;border-radius:3px;font-size:8px;font-weight:500;display:flex;align-items:center;justify-content:center;border:1px solid var(--line);background:var(--white);color:var(--navy)}
.choice .radio{position:absolute;left:7px;width:7px;height:7px}
.choice.selected{background:var(--green);color:var(--white);border-color:var(--green)}
.choice.selected .radio{border:2px solid var(--white)}

.score{left:50px;width:75px;height:16px;border:1px solid var(--line);border-radius:3px;background:var(--white);font-size:7px;color:var(--navy);display:flex;align-items:center;justify-content:center}
.score.selected{background:var(--mint);border-color:var(--green)}

.btn{height:14px;padding:0 7px;font-size:9px;font-weight:500;display:flex;align-items:center;transform:translateX(-50%);border-radius:2px}
.btn.primary{background:var(--green);color:var(--white)}
.btn.back{color:var(--back)}

.progress-label{left:0;right:0;text-align:center;font-size:9px;font-weight:500;color:var(--navy)}
.progress{left:15px;width:151px;height:16px;border-radius:4px;background:var(--track)}
.progress-fill{position:absolute;top:0;left:0;height:16px;border-radius:4px;background:var(--green);color:var(--white);font-size:8px;font-weight:500;display:flex;align-items:center;justify-content:center}

.thanks{top:149px;left:0;right:0;text-align:center;font-size:12px;font-weight:600;color:var(--navy)}

.legal{left:0;right:0;bottom:0;height:22px;background:var(--screen-grey);font-size:5.5px;color:var(--legal);text-align:center;padding-top:5px;line-height:8px}
.legal b{font-weight:600}
</style>
</head>
<body>
<div class="canvas">
  <h1 class="page-title">Survey Webpage Mobile Layout</h1>

  <span class="page-label" style="left:150px;top:103px">Page 1</span>
  <span class="page-label" style="left:472px;top:103px">Page 2</span>
  <span class="page-label" style="left:816px;top:103px">Page 3</span>
  <span class="page-label" style="left:310px;top:588px">Page 4</span>
  <span class="page-label" style="left:634px;top:588px">Page 5</span>

  <!-- Open-end question -->
  <section class="screen" style="left:157px;top:178px;height:318px">
    <svg class="backdrop" viewBox="0 0 180 180"><path d="M0 0H180V92Q125 100 90 128Q55 100 0 92Z"/></svg>
    <div class="brand"><span class="brand-dot"></span><span class="brand-name">NORVANE</span></div>
    <svg class="close" viewBox="0 0 10 10"><circle cx="5" cy="5" r="4.3" fill="none" stroke="#e2a0a6"/><path d="M3 3L7 7M7 3L3 7" stroke="#e2a0a6"/></svg>
    <h2 class="survey-title">CUSTOMER SURVEY</h2>
    <p class="question">How do you feel<br>with this car model?</p>
    <div class="answer-box"></div>
    <span class="btn primary" style="left:90px;top:217px">Next</span>
    <p class="progress-label" style="top:252px">Progress Bar</p>
    <div class="progress" style="top:266px"></div>
    <footer class="legal"><b>Terms of Service</b> and <b>Privacy Policy</b><br><b>@2020</b></footer>
  </section>

  <!-- Single-answer question -->
  <section class="screen" style="left:483px;top:178px;height:363px">
    <svg class="backdrop" viewBox="0 0 180 180"><path d="M0 0H180V92Q125 100 90 128Q55 100 0 92Z"/></svg>
    <div class="brand"><span class="brand-dot"></span><span class="brand-name">NORVANE</span></div>
    <svg class="close" viewBox="0 0 10 10"><circle cx="5" cy="5" r="4.3" fill="none" stroke="#e2a0a6"/><path d="M3 3L7 7M7 3L3 7" stroke="#e2a0a6"/></svg>
    <h2 class="survey-title">CUSTOMER SURVEY</h2>
    <p class="question">Which car model you<br>purchased in the past year?</p>
    <label class="option" style="top:117px"><span class="radio"></span>Solen Pico</label>
    <label class="option" style="top:139px"><span class="radio"></span>Norvane 2</label>
    <label class="option" style="top:161px"><span class="radio"></span>Veltra K400</label>
    <label class="option" style="top:183px"><span class="radio"></span>Veltra SK200</label>
    <label class="option" style="top:205px"><span class="radio"></span>Orlin TR300</label>
    <label class="option wide" style="top:228px"><span class="radio"></span>Others (click and text box expand)</label>
    <span class="btn back" style="left:52px;top:264px">Back</span>
    <span class="btn primary" style="left:124px;top:264px">Next</span>
    <p class="progress-label" style="top:297px">Progress Bar</p>
    <div class="progress" style="top:310px"><div class="progress-fill" style="width:38px">25%</div></div>
    <footer class="legal"><b>Terms of Service</b> and <b>Privacy Policy</b><br><b>@2020</b></footer>
  </section>

  <!-- Yes/No question -->
  <section class="screen warm" style="left:825px;top:177px;height:319px">
    <svg class="backdrop" viewBox="0 0 180 180"><path d="M0 0H180V92Q125 100 90 128Q55 100 0 92Z"/></svg>
    <div class="brand"><span class="brand-dot"></span><span class="brand-name">NORVANE</span></div>
    <svg class="close" viewBox="0 0 10 10"><circle cx="5" cy="5" r="4.3" fill="none" stroke="#e2a0a6"/><path d="M3 3L7 7M7 3L3 7" stroke="#e2a0a6"/></svg>
    <h2 class="survey-title">CUSTOMER SURVEY</h2>
    <p class="question" style="top:80px">Do you own any car?</p>
    <label class="choice selected" style="top:110px"><span class="radio"></span>YES</label>
    <label class="choice" style="top:147px"><span class="radio"></span>NO</label>
    <span class="btn back" style="left:52px;top:217px">Back</span>
    <span class="btn primary" style="left:124px;top:217px">Next</span>
    <p class="progress-label" style="top:251px">Progress Bar</p>
    <div class="progress" style="top:266px"><div class="progress-fill" style="width:75px">50%</div></div>
    <footer class="legal"><b>Terms of Service</b> and <b>Privacy Policy</b><br><b>@2020</b></footer>
  </section>

  <!-- 1-5 scale question -->
  <section class="screen" style="left:320px;top:659px;height:343px">
    <svg class="backdrop" viewBox="0 0 180 180"><path d="M0 0H180V92Q125 100 90 128Q55 100 0 92Z"/></svg>
    <div class="brand"><span class="brand-dot"></span><span class="brand-name">NORVANE</span></div>
    <svg class="close" viewBox="0 0 10 10"><circle cx="5" cy="5" r="4.3" fill="none" stroke="#e2a0a6"/><path d="M3 3L7 7M7 3L3 7" stroke="#e2a0a6"/></svg>
    <h2 class="survey-title">CUSTOMER SURVEY</h2>
    <p class="question">Please rate your<br>satisfaction score.</p>
    <span class="score" style="top:118px">5</span>
    <span class="score selected" style="top:140px">4</span>
    <span class="score" style="top:163px">3</span>
    <span class="score" style="top:185px">2</span>
    <span class="score" style="top:207px">1</span>
    <span class="btn back" style="left:52px;top:243px">Back</span>
    <span class="btn primary" style="left:124px;top:243px">Done</span>
    <p class="progress-label" style="top:277px">Progress Bar</p>
    <div class="progress" style="top:292px"><div class="progress-fill" style="width:114px">75%</div></div>
    <footer class="legal"><b>Terms of Service</b> and <b>Privacy Policy</b><br><b>@2020</b></footer>
  </section>

  <!-- Thank you page -->
  <section class="screen" style="left:644px;top:659px;height:318px">
    <svg class="backdrop" viewBox="0 0 180 180"><path d="M0 0H180V96Q125 110 90 170Q55 110 0 96Z"/></svg>
    <div class="brand"><span class="brand-dot"></span><span class="brand-name">NORVANE</span></div>
    <svg class="close" viewBox="0 0 10 10"><circle cx="5" cy="5" r="4.3" fill="none" stroke="#e2a0a6"/><path d="M3 3L7 7M7 3L3 7" stroke="#e2a0a6"/></svg>
    <h2 class="survey-title">CUSTOMER SURVEY</h2>
    <p class="thanks">Thanks for your Survey !</p>
    <p class="progress-label" style="top:251px">Progress Bar</p>
    <div class="progress" style="top:266px"><div class="progress-fill" style="width:151px">100%</div></div>
    <footer class="legal"><b>Terms of Service</b> and <b>Privacy Policy</b><br><b>@2020</b></footer>
  </section>
</div>
</body>
</html>
```